Trifold for International Business Consulting firm

I have created a trifold piece (attached) that includes all the necessary information in a Word template; however, I need a professional that can make it look "current, international and modern". Our website, brenvaleadvisory.com, should give an idea as to the style and color template we like.

```html
<!DOCTYPE html>
<html lang="en">
<head>
<meta charset="utf-8">
<title>Brenvale Advisory – Trifold Outside</title>
<link href="https://fonts.googleapis.com/css2?family=Montserrat:wght@400;600;700&family=Questrial&display=swap" rel="stylesheet">
<style>
  :root{
    --stage:#e4e4e4;
    --slate:#55595b;
    --slate-dark:#3f4244;
    --lime:#a5cd39;
    --lime-bright:#c9d92a;
    --ink:#2b2d2e;
    --paper:#ffffff;
    --soft:#d9dcdc;
  }
  *{box-sizing:border-box;margin:0;padding:0}
  html,body{width:1200px;height:1000px;overflow:hidden;background:var(--stage)}
  body{font-family:"Questrial",sans-serif;color:var(--paper)}
  .trifold{position:absolute;left:150px;top:150px;width:900px;height:700px;display:flex;box-shadow:0 8px 24px rgba(0,0,0,.18)}
  .panel{position:relative;width:300px;height:700px;background:var(--slate);overflow:hidden}
  .panel + .panel{border-left:1px solid rgba(0,0,0,.12)}

  /* back flap */
  .flap-photo{position:absolute;left:0;top:0}
  .services-title{position:absolute;left:128px;top:22px;width:160px;font-family:"Montserrat",sans-serif;font-weight:600;font-size:17px;line-height:1.2}
  .steps-label{position:absolute;left:128px;top:84px;font-family:"Montserrat",sans-serif;font-weight:700;font-size:11px;letter-spacing:.5px;display:flex;align-items:center;gap:3px}
  .steps-label .big{font-size:34px;color:var(--lime);line-height:1}
  .steps-intro{position:absolute;left:128px;top:128px;width:160px;font-size:11px;line-height:1.35;color:var(--soft)}
  .step-list{position:absolute;left:22px;top:200px;width:260px;list-style:none}
  .step-list li{display:flex;align-items:center;gap:14px;margin-bottom:14px;font-size:11px;line-height:1.3;color:var(--soft)}
  .step-num{flex:none;width:30px;height:30px;border-radius:50%;background:var(--paper);color:var(--slate);font-size:20px;display:flex;align-items:center;justify-content:center}
  .process-band{position:absolute;left:0;top:350px;width:300px;height:200px}
  .band-text{position:absolute;left:18px;top:372px;width:266px;font-size:11px;line-height:1.35}
  .band-text .lead{text-transform:uppercase;color:var(--paper);font-size:12px}
  .band-text .strong{text-transform:uppercase;color:var(--ink);font-family:"Montserrat",sans-serif;font-weight:700;font-size:11.5px;margin-bottom:4px}
  .band-text p{color:var(--ink)}
  .follow{position:absolute;left:18px;top:512px;display:flex;align-items:center;gap:8px;font-size:11px;text-transform:uppercase;color:var(--paper)}
  .social-square{width:14px;height:14px;background:var(--slate-dark)}
  .legal{position:absolute;left:18px;top:580px;font-size:9px;color:var(--soft)}

  /* photo spread across middle and cover */
  .spread-photo{position:absolute;left:450px;top:150px;width:600px;height:700px}
  .brand-name{font-family:"Montserrat",sans-serif;font-weight:700;text-transform:uppercase;letter-spacing:1px}
  .contact{position:absolute;left:22px;top:26px;width:260px}
  .contact .brand-name{font-size:15px;color:var(--paper);margin-bottom:14px}
  .contact-line{display:flex;align-items:flex-start;gap:7px;font-size:11px;line-height:1.35;margin-bottom:5px}
  .contact-line svg{flex:none;margin-top:1px}
  .contact-web{font-family:"Montserrat",sans-serif;font-weight:600;font-size:12px;margin-top:12px}
  .contact-web span{font-weight:400;color:var(--soft)}

  /* cover */
  .cover-label{position:absolute;left:18px;top:410px;width:250px;height:100px;background:var(--paper);display:flex;align-items:center;padding-left:16px}
  .cover-label .brand-name{font-size:21px;color:var(--ink);line-height:1.1}
  .cover-corner{position:absolute;left:232px;top:410px}
  .cover-tagline{position:absolute;left:18px;top:510px;width:270px;height:26px;background:var(--lime-bright);color:var(--ink);font-family:"Montserrat",sans-serif;font-size:11px;display:flex;align-items:center;padding-left:16px;text-transform:uppercase}
  .cover-tagline b{font-weight:700;margin-left:4px}
  .cover-web{position:absolute;left:22px;top:560px;font-family:"Montserrat",sans-serif;font-weight:600;font-size:12px}
  .cover-web span{font-weight:400}
  .panel-layer{position:absolute;inset:0}
  .middle, .cover{background:transparent}
</style>
</head>
<body>
<svg class="spread-photo" width="600" height="700" viewBox="0 0 600 700" role="img" aria-label="Photograph of industrial building facade with rows of steel pipes, grey on the inside panel and green-tinted on the cover">
  <defs>
    <linearGradient id="pipesGrey" x1="0" y1="0" x2="1" y2="1">
      <stop offset="0" stop-color="#9a9d9e"/>
      <stop offset=".5" stop-color="#6c7072"/>
      <stop offset="1" stop-color="#4a4d4f"/>
    </linearGradient>
    <linearGradient id="pipesGreen" x1="0" y1="0" x2="1" y2="1">
      <stop offset="0" stop-color="#8fb3a0"/>
      <stop offset=".5" stop-color="#5d7f70"/>
      <stop offset="1" stop-color="#2f4039"/>
    </linearGradient>
  </defs>
  <rect x="0" y="0" width="300" height="700" fill="url(#pipesGrey)"/>
  <rect x="300" y="0" width="300" height="700" fill="url(#pipesGreen)"/>
  <path d="M0 0 H430 Q300 250 0 460 Z" fill="#55595b"/>
  <path d="M0 460 Q300 250 430 0" fill="none" stroke="#c9d92a" stroke-width="4"/>
</svg>

<main class="trifold">
  <section class="panel back-flap">
    <svg class="flap-photo" width="130" height="170" viewBox="0 0 130 170" role="img" aria-label="Cropped photograph of steel pipes">
      <defs>
        <linearGradient id="flapPipes" x1="0" y1="0" x2="1" y2="1">
          <stop offset="0" stop-color="#8fb3a0"/>
          <stop offset="1" stop-color="#4f6b5f"/>
        </linearGradient>
      </defs>
      <polygon points="0,0 120,0 60,170 0,170" fill="url(#flapPipes)"/>
      <polygon points="120,0 60,170 48,150 104,0" fill="#a5cd39"/>
    </svg>
    <h2 class="services-title">Comprehensive Services Business Development</h2>
    <div class="steps-label">Our <span class="big">3</span> Steps Process</div>
    <p class="steps-intro">Once you have made the decision to grow your business internationally we follow a very simple and cost efficient path.</p>
    <ol class="step-list">
      <li><span class="step-num">1</span>Gather necessary information.</li>
      <li><span class="step-num">2</span>Perform an onsite company readiness check and presentation.</li>
      <li><span class="step-num">3</span>Develop and provide an international strategic path forward.</li>
    </ol>
    <svg class="process-band" width="300" height="200" viewBox="0 0 300 200" aria-hidden="true">
      <polygon points="0,0 130,0 150,18 170,0 300,0 300,200 0,200" fill="#a5cd39"/>
    </svg>
    <div class="band-text">
      <div class="lead">Let us manage the entire process for you</div>
      <div class="strong">From strategy to successful execution.</div>
      <p>We will assemble and coordinate the needed team of specialists for the project and provide the necessary business contacts for your international growth.</p>
    </div>
    <div class="follow">Follow us on <span class="social-square"></span><span class="social-square"></span></div>
    <div class="legal">©Calloway Integrators, LLC</div>
  </section>

  <section class="panel middle">
    <div class="contact">
      <div class="brand-name">Brenvale Advisory</div>
      <div class="contact-line">
        <svg width="10" height="13" viewBox="0 0 10 13"><path d="M5 0a5 5 0 0 1 5 5c0 3.5-5 8-5 8S0 8.5 0 5a5 5 0 0 1 5-5z" fill="#fff"/><circle cx="5" cy="5" r="2" fill="#55595b"/></svg>
        <span>418 Harlow Ave. Suite 120<br>Riverton, TX 78051</span>
      </div>
      <div class="contact-line">
        <svg width="11" height="11" viewBox="0 0 11 11"><circle cx="5.5" cy="5.5" r="5" fill="none" stroke="#fff"/><path d="M3.5 3l1.2-.3.6 1.4-.7.5a4 4 0 0 0 1.8 1.8l.5-.7 1.4.6-.3 1.2C5.8 7.5 3.5 5.2 3.5 3z" fill="#fff"/></svg>
        <span>+1 555 014 2290</span>
      </div>
      <div class="contact-line">
        <svg width="11" height="9" viewBox="0 0 11 9"><rect width="11" height="9" rx="1" fill="#fff"/><path d="M0.5 1l5 4 5-4" fill="none" stroke="#55595b"/></svg>
        <span>info@brenvaleadvisory.com</span>
      </div>
      <div class="contact-web">brenvaleadvisory<span>.com</span></div>
    </div>
  </section>

  <section class="panel cover">
    <svg class="cover-corner" width="60" height="100" viewBox="0 0 60 100" aria-hidden="true">
      <polygon points="36,30 60,0 60,60" fill="#a5cd39"/>
    </svg>
    <div class="cover-label"><span class="brand-name">Brenvale<br>Advisory</span></div>
    <div class="cover-tagline">International business <b>development</b></div>
    <div class="cover-web">brenvaleadvisory<span>.com</span></div>
  </section>
</main>
</body>
</html>
```